PawCrate Banner contest an ecommerce site for veterinarians

We need banners for our ecommerce site. Our site is a webstore that veterinarians can use to allow their clients to purchase items from them. Each month we have a different theme for our banners. I am looking for banners for January and February and with a refresh coming to our site could be looking at a dozen over the next year. I may potentially choose from multiple designers and increase the payment or will choose one designer for both months .

For January our theme is winter fun. We will be running a contest were people can submit a picture of their pet to our Chirpbook page enjoying the snow or keeping warm. they have a chance to win one of 5 $50 gift certificates to pawcrate. The banner should have a dog and cat and a separate one with just a cat. We will need a French and English banner. We will provide the French translation once the winner has been selected.

For February our theme is dental health. The banner should have a dog and cat and a separate one with just a cat. We will need a French and English banner. We will provide the French translation once the winner has been selected.

Target Market(s)

pet owners

Industry/Entity Type

Veterinary

Colors

Designer to choose colors to be used in the design.

Requirements
Must have
• dimensions for PCR Banner are: 710px x 280px
Nice to have
• I have attached our logo and some screen shoots of our site so you can get a feel of what it look like. you could also go to www.pawcrate-example.ca and see what the sign in page looks like
Should not have
• images of pet food

```html
<!DOCTYPE html>
<html lang="en">
<head>
<meta charset="utf-8">
<title>Winter Fun Banner – PawCrate</title>
<link href="https://fonts.googleapis.com/css2?family=Mountains+of+Christmas:wght@700&family=Oswald:wght@400;600;700&display=swap" rel="stylesheet">
<style>
  :root {
    --stage: #272727;
    --sky: #e6eaec;
    --snow: #f9f6ef;
    --snow-shade: #eef0ef;
    --title-grey: #7b7b7b;
    --teal: #237a90;
    --red: #c01e2e;
    --ink: #1f1f1f;
    --logo-grey: #4a4a4a;
    --photo-light: #dfe6ea;
    --photo-mid: #a9b6bf;
    --photo-dark: #5a5048;
  }
  * { margin: 0; padding: 0; box-sizing: border-box; }
  html, body {
    width: 1200px; height: 1200px; overflow: hidden;
    background: var(--stage);
  }
  .banner {
    position: absolute;
    left: 149px; top: 416px;
    width: 888px; height: 350px;
    overflow: hidden;
    background: linear-gradient(180deg, var(--sky) 0%, #eef1f1 60%, var(--snow) 100%);
    font-family: "Oswald", "Arial Narrow", sans-serif;
  }
  .banner__snowdrift {
    position: absolute; left: 0; top: 0; width: 888px; height: 350px;
  }
  .banner__photo {
    position: absolute; right: 0; top: 0;
    width: 480px; height: 350px;
    background:
      radial-gradient(ellipse 90px 130px at 330px 150px, var(--photo-dark) 0%, rgba(90,80,72,0.7) 55%, rgba(90,80,72,0) 100%),
      radial-gradient(ellipse 55px 45px at 190px 200px, rgba(120,110,100,0.75) 0%, rgba(120,110,100,0) 100%),
      linear-gradient(180deg, var(--photo-light) 0%, var(--photo-mid) 45%, var(--snow-shade) 72%, var(--snow) 100%);
    -webkit-mask-image: linear-gradient(90deg, transparent 0%, #000 30%);
            mask-image: linear-gradient(90deg, transparent 0%, #000 30%);
  }
  .promo {
    position: absolute; left: 0; top: 0;
    width: 516px; height: 350px;
    text-align: center;
  }
  .promo__title {
    position: absolute; left: 0; right: 0; top: 44px;
    font-family: "Mountains of Christmas", "Georgia", serif;
    font-weight: 700; font-size: 56px; line-height: 1;
    letter-spacing: 1px;
    color: var(--title-grey);
  }
  .promo__lead {
    position: absolute; left: 0; right: 0; top: 116px;
    font-weight: 600; font-size: 29px; line-height: 1;
    color: var(--teal);
  }
  .promo__prize {
    position: absolute; left: 0; right: 0; top: 151px;
    font-weight: 700; font-size: 50px; line-height: 1;
    letter-spacing: -0.5px;
    color: var(--red);
  }
  .promo__store {
    position: absolute; left: 0; right: 0; top: 203px;
    font-weight: 600; font-size: 29px; line-height: 1;
    color: var(--teal);
  }
  .promo__details {
    position: absolute; left: 0; right: 0; top: 250px;
    font-weight: 400; font-size: 21px; line-height: 28px;
    color: var(--ink);
  }
  .brand {
    position: absolute; left: 680px; top: 292px;
    display: flex; align-items: center; gap: 8px;
    font-family: "Oswald", "Arial Narrow", sans-serif;
    font-weight: 400; font-size: 30px; line-height: 1;
    color: var(--logo-grey);
  }
  .brand__dot {
    width: 12px; height: 12px; border-radius: 50%;
    background: var(--logo-grey);
  }
</style>
</head>
<body>
  <section class="banner">
    <div class="banner__photo" role="img" aria-label="Photo of a dog and a cat sitting in deep snow beneath bare snowy branches"></div>
    <svg class="banner__snowdrift" viewBox="0 0 888 350" aria-hidden="true">
      <path d="M0 205 C 90 196, 170 198, 260 206 C 360 214, 440 205, 560 232 L 560 350 L 0 350 Z" fill="var(--snow)" opacity="0.95"/>
      <path d="M520 290 C 620 270, 720 272, 888 280 L 888 350 L 520 350 Z" fill="var(--snow)" opacity="0.9"/>
    </svg>
    <div class="promo">
      <h1 class="promo__title">WINTER FUN</h1>
      <p class="promo__lead">GET A CHANCE TO WIN ONE OF 5</p>
      <p class="promo__prize">$50 GIFT CERTIFICATES</p>
      <p class="promo__store">TO PAWCRATE</p>
      <p class="promo__details">Submit a picture of your PET to our Chirpbook page<br>enjoying the snow or keeping warm</p>
    </div>
    <div class="brand"><span class="brand__dot"></span><span class="brand__name">pawcrate</span></div>
  </section>
</body>
</html>
```